We need a business card design for a new brand within our existing financial marketing business. Our new brand is www.quellpath.co.uk

We attach various logo files - please use the version that will produce the sharpest image on the business card.

We are flexible about shape of card etc. Please think outside the box as to what goes on front and what goes on back of the card.

The card needs to be corporate, but really catch the eye ( e.g. premium translucent cards on plastic etc or metal cards or shiny surface etc )

We want to be able to amend the card (once the design has been agreed ) to add additional staff details, but the text to go on it will be generic

Details to go on card ( for the first generic one) are fairly minimal as we don't like cluttered business cards:-

Owen Tabler
Managing Director

Mobile: 07841 552 078
Email: o.tabler@quellpath.co.uk

```html
<!DOCTYPE html>
<html lang="en">
<head>
<meta charset="utf-8">
<title>quellpath business card</title>
<link rel="stylesheet" href="https://fonts.googleapis.com/css2?family=Ubuntu:wght@300;400;700&display=swap">
<style>
  :root {
    --backdrop: #e4e4e2;
    --card-white: #ffffff;
    --card-dark: #2b2a28;
    --brand-blue: #2f62b8;
    --brand-yellow: #d6b21a;
    --text-light: #f4f4f2;
  }
  * { box-sizing: border-box; margin: 0; padding: 0; }
  html, body {
    width: 1200px; height: 873px; overflow: hidden;
    background: var(--backdrop);
    font-family: "Ubuntu", sans-serif;
  }
  .sheet {
    position: relative; width: 1200px; height: 873px;
    display: flex; align-items: center; justify-content: center; gap: 60px;
  }
  .card {
    position: relative; width: 500px; height: 286px;
    border-radius: 4px; overflow: hidden;
    box-shadow: 0 10px 30px rgba(0,0,0,.18);
  }
  /* front */
  .card-front { background: var(--card-white); }
  .edge-band {
    position: absolute; left: 0; top: 0; width: 16px; height: 100%;
    display: flex; flex-direction: column;
  }
  .edge-band .band-top { flex: 1; background: var(--brand-yellow); }
  .edge-band .band-bottom { flex: 1; background: var(--brand-blue); }
  .person { position: absolute; left: 48px; top: 38px; }
  .person-name { color: var(--brand-blue); font-weight: 700; font-size: 24px; line-height: 1.1; }
  .person-role {
    color: var(--brand-yellow); font-size: 11px; font-variant: small-caps;
    letter-spacing: .5px; margin-top: 3px;
  }
  .wordmark {
    position: absolute; display: flex; align-items: center; gap: 10px;
  }
  .card-front .wordmark { right: 42px; top: 118px; }
  .wordmark .mark-square { width: 30px; height: 30px; background: var(--brand-yellow); }
  .wordmark .brand-name { font-weight: 300; font-size: 46px; line-height: 1; }
  .card-front .brand-name { color: var(--brand-blue); }
  .contact-list {
    position: absolute; right: 42px; bottom: 30px; list-style: none;
    display: flex; flex-direction: column; gap: 6px;
  }
  .contact-list li {
    display: flex; align-items: center; gap: 8px;
    color: var(--brand-yellow); font-size: 14px;
  }
  .contact-icon { width: 16px; height: 16px; flex: none; }
  /* back */
  .card-back {
    background: radial-gradient(circle at 35% 30%, #3a3936 0%, var(--card-dark) 70%);
    display: flex; align-items: center; justify-content: center;
  }
  .card-back .wordmark { position: static; }
  .card-back .brand-name { color: var(--text-light); font-size: 58px; }
</style>
</head>
<body>
<main class="sheet">
  <section class="card card-front" aria-label="Card front">
    <div class="edge-band"><span class="band-top"></span><span class="band-bottom"></span></div>
    <div class="person">
      <p class="person-name">Owen Tabler</p>
      <p class="person-role">Managing Director</p>
    </div>
    <div class="wordmark">
      <span class="mark-square"></span>
      <span class="brand-name">quellpath</span>
    </div>
    <ul class="contact-list">
      <li>
        <svg class="contact-icon" viewBox="0 0 16 16" aria-hidden="true"><circle cx="8" cy="8" r="8" fill="#2f62b8"/><path d="M5.5 4.5l1.5 0 .7 1.8-.9.7a4.5 4.5 0 0 0 2.2 2.2l.7-.9 1.8.7 0 1.5c-3.5.3-6.3-2.5-6-6z" fill="#fff"/></svg>
        07841 552 078
      </li>
      <li>
        <svg class="contact-icon" viewBox="0 0 16 16" aria-hidden="true"><circle cx="8" cy="8" r="8" fill="#2f62b8"/><rect x="4" y="5" width="8" height="6" fill="none" stroke="#fff" stroke-width="1"/><path d="M4 5l4 3.3L12 5" fill="none" stroke="#fff" stroke-width="1"/></svg>
        o.tabler@quellpath.co.uk
      </li>
      <li>
        <svg class="contact-icon" viewBox="0 0 16 16" aria-hidden="true"><circle cx="8" cy="8" r="8" fill="#2f62b8"/><circle cx="8" cy="8" r="4.2" fill="none" stroke="#fff" stroke-width="1"/><path d="M3.8 8h8.4M8 3.8c-2 2.5-2 5.9 0 8.4M8 3.8c2 2.5 2 5.9 0 8.4" fill="none" stroke="#fff" stroke-width=".8"/></svg>
        www.quellpath.co.uk
      </li>
    </ul>
  </section>
  <section class="card card-back" aria-label="Card back">
    <div class="wordmark">
      <span class="brand-name">quellpath</span>
    </div>
  </section>
</main>
</body>
</html>
```